App for Lawyers & Accountants needs 'Professional' Styling

We want to style our app to convey a 'Professional' appearance. It's used by Lawyers, Accountants, Doctors etc. who take their work very seriously.

We currently trying to follow keystrel layout guidelines, but we find our app looks very bland. I've uploaded a screenshot of our current app, and two mock-ups of more stylized versions, but we're not happy with those mock-ups.

We'd like to see alternate designs for those two mock-ups, that look much more professional.

The specific elements we'd like to improve/focus on are:
* Colour of the top and left nav bars
* Appearance of the left nav, size, icons spacing
* Appearance of the buttons on the top right, so the user knows they are buttons they can press
* Spacing of the dashboard, background colour and spacing, colour/layout of the 'overdue' and 'todo' accordion headings in the 'my tasks' section.
* List view background grey, to be consistent with dashboard, but unobtrusive
* List view tabs to be obvious as tabs, but 'saved searches', filters and the export icon to still be associated with the data displayed, but it should be obvious to the user that those are different buttons, not just more tabs. (I.e. the filters button opens a panel below it that allows the user to filter the data in the list.)
* General appearance of the popup menu when you push the 'add' button on the top right

However, despite those specifics I'm sure it's all the subtle elements of the design that make a big difference.

Our brand colour is 1D4F91, and we use A20067 as a secondary colour in print media, (although it doesn't seem to work to well within the app.) Our brand font is signika. We'd like the designs to be based on those colours & font.

Target Market(s)

Professional people, Lawyers, Accountants, Doctors etc.

Font styles to use
Sans Serif
Other font styles liked:
• Signika

Colors
0255a3

Requirements
Must have
• The most 'Professional' experience/quality possible. Think the quality & brand image of vantrel desk, but taken to a higher level.
• An example/mock-up of the dashboard, list view and 'add' item popup menu
• Display the dashboard cards with the same information as our mock-ups - the information there is important and we don't have any extra cards to add (in the near term)
Nice to have
• Various colour combinations for the top and left nav bars, based on our primary blue brand colour, and perhaps some shade of dark grey.

```html
<!DOCTYPE html>
<html lang="en">
<head>
<meta charset="utf-8">
<title>My Matters</title>
<link rel="stylesheet" href="https://fonts.googleapis.com/css2?family=Fira+Sans:wght@400;500;600&display=swap">
<style>
:root{
  --bg:#f4f5f8;
  --surface:#ffffff;
  --line:#e6e8ee;
  --line-strong:#dde0e8;
  --brand:#1D4F91;
  --accent:#A20067;
  --accent-soft:#f8c9e6;
  --icon-muted:#dde1e8;
  --text-strong:#3b414c;
  --text-head:#5e6a79;
  --text-muted:#8a96a4;
  --text-faint:#c9ced7;
  --menu-text:#5d6c7f;
}
*{box-sizing:border-box;margin:0;padding:0}
html,body{width:1200px;height:908px;overflow:hidden;background:var(--bg)}
body{font-family:"Fira Sans",sans-serif}
.app{position:relative;width:1280px;height:969px;transform:scale(.9375);transform-origin:0 0;background:var(--bg)}
.topbar{position:absolute;left:0;top:0;width:1280px;height:68px;background:var(--surface);border-bottom:1px solid var(--line)}
.sidebar{position:absolute;left:0;top:68px;width:72px;height:901px;background:var(--surface);border-right:1px solid var(--line)}
.menu-toggle{position:absolute;left:0;top:0;width:72px;height:68px;border-right:1px solid var(--line);display:flex;align-items:center;justify-content:center}
.search{position:absolute;left:108px;top:22px;display:flex;align-items:center;gap:14px;font-size:16px;color:var(--text-faint)}
.divider{position:absolute;top:0;width:1px;height:68px;background:var(--line)}
.add-btn{position:absolute;left:824px;top:24px;display:flex;align-items:center;gap:6px;color:var(--brand);font-size:15px;font-weight:500}
.top-icon{position:absolute;top:25px}
.user{position:absolute;left:1046px;top:17px;display:flex;align-items:center;gap:15px;font-size:13px;color:var(--text-strong)}
.avatar{width:36px;height:36px;border-radius:50%;background:linear-gradient(135deg,#c9b7a6,#6e7a86)}
.caret{position:absolute;left:1238px;top:32px}
.nav-icon{position:absolute;left:26px}
.nav-active{position:absolute;left:69px;top:192px;width:3px;height:45px;background:var(--brand)}
.card{position:absolute;left:110px;top:107px;width:1132px;height:824px;background:var(--surface);box-shadow:0 2px 8px rgba(40,50,70,.06)}
.tabs{position:absolute;left:60px;top:74px;width:1012px;height:54px;border-bottom:3px solid var(--line-strong)}
.tab{position:absolute;top:6px;font-size:16px;color:var(--text-faint)}
.tab.active{color:var(--text-strong);font-weight:600}
.tab-indicator{position:absolute;left:0;bottom:-3px;width:90px;height:3px;background:var(--accent)}
.tool-btn{position:absolute;top:72px;width:38px;height:37px;border:1px solid var(--line-strong);background:var(--surface);display:flex;align-items:center;justify-content:center}
.matters{position:absolute;left:80px;top:178px;width:972px}
.row{display:flex;height:77px;align-items:center;border-bottom:1px solid var(--line-strong);font-size:16px;color:var(--text-muted)}
.row.head{height:38px;border:0;font-size:15px;font-weight:600;color:var(--text-head);margin-bottom:20px;align-items:flex-start}
.c1{width:402px}.c2{width:152px}.c3{width:173px}.c4{width:150px}.c5{flex:1;white-space:nowrap}
.row:not(.head) .c1{color:var(--text-strong)}
.pager{position:absolute;left:461px;top:738px;display:flex;align-items:center;gap:10px}
.page{width:28px;height:28px;display:flex;align-items:center;justify-content:center;font-size:14px;background:var(--accent-soft);color:var(--accent)}
.page.current{background:var(--accent);color:#fff;font-weight:600}
.next{margin-left:10px;display:flex;align-items:center;gap:6px;color:var(--accent);font-size:15px}
.add-menu{position:absolute;left:597px;top:45px;width:231px;height:330px;background:var(--surface);box-shadow:0 4px 18px rgba(40,50,70,.14);padding-top:10px}
.add-item{display:flex;align-items:center;height:51px;padding-left:28px;gap:18px;font-size:18px;color:var(--menu-text)}
.add-item svg{width:24px;height:24px}
</style>
</head>
<body>
<div class="app">
  <header class="topbar">
    <div class="menu-toggle">
      <svg width="18" height="14" viewBox="0 0 18 14" fill="#c9ced7"><rect width="18" height="2.4"/><rect y="5.5" width="18" height="2.4"/><rect y="11" width="12" height="2.4"/></svg>
    </div>
    <div class="search">
      <svg width="20" height="20" viewBox="0 0 20 20" fill="none" stroke="#c9ced7" stroke-width="2"><circle cx="8" cy="8" r="6"/><path d="M12.5 12.5l5.5 5.5"/></svg>
      <span>Search Something....</span>
    </div>
    <span class="divider" style="left:804px"></span>
    <div class="add-btn">
      <svg width="14" height="14" viewBox="0 0 14 14" stroke="#1D4F91" stroke-width="2"><path d="M7 0v14M0 7h14"/></svg>Add
    </div>
    <span class="divider" style="left:893px"></span>
    <svg class="top-icon" style="left:921px" width="19" height="19" viewBox="0 0 20 20" fill="none" stroke="#c9ced7" stroke-width="2"><path d="M17 10a7 7 0 1 1-2-5M17 2v4h-4"/><path d="M10 6v4l3 2"/></svg>
    <span class="divider" style="left:961px"></span>
    <svg class="top-icon" style="left:986px" width="20" height="20" viewBox="0 0 20 20"><path d="M10 3a5 5 0 0 0-5 5v4l-2 3h14l-2-3V8a5 5 0 0 0-5-5z" fill="none" stroke="#c9ced7" stroke-width="1.8"/><path d="M8 17a2 2 0 0 0 4 0" stroke="#c9ced7" stroke-width="1.8" fill="none"/><circle cx="15" cy="4" r="3" fill="#1D4F91"/></svg>
    <span class="divider" style="left:1030px"></span>
    <div class="user"><div class="avatar" role="img" aria-label="User profile photo"></div><span>Dorian Halvek</span></div>
    <svg class="caret" width="10" height="6" viewBox="0 0 10 6" fill="#c9ced7"><path d="M0 0h10L5 6z"/></svg>
  </header>

  <nav class="sidebar">
    <svg class="nav-icon" style="top:61px" width="22" height="22" viewBox="0 0 22 22" fill="#dde1e8"><path d="M11 2L1 11h3v9h5v-6h4v6h5v-9h3z"/></svg>
    <svg class="nav-icon" style="top:128px" width="24" height="24" viewBox="0 0 24 24" fill="#dde1e8"><path d="M9 2l7 7-3 3-7-7zM11 10l-9 9 2 2 9-9zM12 21h10v2H12z"/></svg>
    <svg class="nav-icon" style="top:195px" width="22" height="22" viewBox="0 0 22 22" fill="#1D4F91"><circle cx="11" cy="6" r="5"/><path d="M1 21c0-6 4-8 10-8s10 2 10 8z"/></svg>
    <span class="nav-active"></span>
    <svg class="nav-icon" style="top:262px" width="22" height="22" viewBox="0 0 22 22" fill="#dde1e8"><path d="M11 1a7 7 0 0 0-7 7v5l-2 4h18l-2-4V8a7 7 0 0 0-7-7zM8 19a3 3 0 0 0 6 0z"/></svg>
    <svg class="nav-icon" style="top:330px" width="22" height="24" viewBox="0 0 22 24" fill="none" stroke="#dde1e8" stroke-width="2.4"><path d="M15 7v10a4 4 0 0 1-8 0V5a3 3 0 0 1 6 0v11a1 1 0 0 1-2 0V7"/></svg>
    <svg class="nav-icon" style="top:400px" width="22" height="22" viewBox="0 0 22 22" fill="none" stroke="#dde1e8" stroke-width="2.4"><circle cx="11" cy="11" r="9"/><path d="M11 5v6l4 3"/></svg>
    <svg class="nav-icon" style="top:516px" width="22" height="22" viewBox="0 0 22 22" fill="#dde1e8"><path d="M9 1h4l1 3 3 1 3-1 2 3-2 3v2l2 3-2 3-3-1-3 1-1 3H9l-1-3-3-1-3 1-2-3 2-3v-2L0 7l2-3 3 1 3-1z"/><circle cx="11" cy="11" r="3.5" fill="#fff"/></svg>
    <svg class="nav-icon" style="top:585px" width="22" height="22" viewBox="0 0 22 22" fill="none" stroke="#dde1e8" stroke-width="2.6"><path d="M12 2H3v18h9M9 11h12M17 7l4 4-4 4"/></svg>
  </nav>

  <main class="card">
    <div class="tabs">
      <span class="tab active" style="left:5px">My Matters</span>
      <span class="tab" style="left:159px">Recent Matters</span>
      <span class="tab" style="left:343px">All Matters</span>
      <span class="tab-indicator"></span>
    </div>
    <div class="tool-btn" style="left:935px"><svg width="24" height="22" viewBox="0 0 24 22" fill="none" stroke="#A20067" stroke-width="2"><path d="M10 19H2V3h7l2 3h10v5"/><circle cx="16" cy="15" r="4"/><path d="M19 18l3 3"/></svg></div>
    <div class="tool-btn" style="left:984px"><svg width="20" height="20" viewBox="0 0 20 20" stroke="#A20067" stroke-width="2"><path d="M4 1v18M10 1v18M16 1v18M1 13h6M7 6h6M13 11h6"/></svg></div>
    <div class="tool-btn" style="left:1033px"><svg width="22" height="20" viewBox="0 0 22 20" fill="none" stroke="#A20067" stroke-width="2"><path d="M13 2H2v16h11M8 10h13M17 6l4 4-4 4"/></svg></div>

    <div class="matters">
      <div class="row head"><span class="c1">Title</span><span class="c2">Client</span><span class="c3">Practice Area</span><span class="c4">Status</span><span class="c5">Last Updated</span></div>
      <div class="row"><span class="c1">Ashcombe vs Veridane Concerning Sales # 502</span><span class="c2">Harlan Fenwick</span><span class="c3">Legal Rights</span><span class="c4">Settelment</span><span class="c5">April 3, 2018</span></div>
      <div class="row"><span class="c1">Ashcombe vs Veridane Concerning Sales # 502</span><span class="c2">Harlan Fenwick</span><span class="c3">Legal Rights</span><span class="c4">Settelment</span><span class="c5">April 3, 2018</span></div>
      <div class="row"><span class="c1">Ashcombe vs Veridane Concerning Sales # 502</span><span class="c2">Harlan Fenwick</span><span class="c3">Legal Rights</span><span class="c4">Settelment</span><span class="c5">April 3, 2018</span></div>
      <div class="row"><span class="c1">Ashcombe vs Veridane Concerning Sales # 502</span><span class="c2">Harlan Fenwick</span><span class="c3">Legal Rights</span><span class="c4">Settelment</span><span class="c5">April 3, 2018</span></div>
      <div class="row"><span class="c1">Ashcombe vs Veridane Concerning Sales # 502</span><span class="c2">Harlan Fenwick</span><span class="c3">Legal Rights</span><span class="c4">Settelment</span><span class="c5">April 3, 2018</span></div>
      <div class="row"><span class="c1">Ashcombe vs Veridane Concerning Sales # 502</span><span class="c2">Harlan Fenwick</span><span class="c3">Legal Rights</span><span class="c4">Settelment</span><span class="c5">April 3, 2018</span></div>
    </div>

    <div class="pager">
      <span class="page current">1</span><span class="page">2</span><span class="page">3</span><span class="page">4</span>
      <span class="next">Next <svg width="8" height="12" viewBox="0 0 8 12" fill="none" stroke="#A20067" stroke-width="2"><path d="M2 1l5 5-5 5"/></svg></span>
    </div>
  </main>

  <div class="add-menu">
    <div class="add-item"><svg viewBox="0 0 24 24" fill="none" stroke="#9aa5b3" stroke-width="1.8"><circle cx="12" cy="12" r="9"/><path d="M12 7v5l3 2"/></svg>Time</div>
    <div class="add-item"><svg viewBox="0 0 24 24" fill="none" stroke="#9aa5b3" stroke-width="1.8"><path d="M15 7v10a3 3 0 0 1-6 0V5a2 2 0 0 1 4 0v11a1 1 0 0 1-2 0V7"/></svg>Documents</div>
    <div class="add-item"><svg viewBox="0 0 24 24" fill="none" stroke="#9aa5b3" stroke-width="1.8"><path d="M12 3a6 6 0 0 0-6 6v5l-2 3h16l-2-3V9a6 6 0 0 0-6-6zM10 20a2 2 0 0 0 4 0"/></svg>Task</div>
    <div class="add-item"><svg viewBox="0 0 24 24" fill="none" stroke="#9aa5b3" stroke-width="1.8"><path d="M5 3h9l5 5v13H5zM14 3v5h5"/></svg>Notes</div>
    <div class="add-item"><svg viewBox="0 0 24 24" fill="none" stroke="#9aa5b3" stroke-width="1.8"><path d="M9 2l6 6-3 3-6-6zM10 9l-8 8 2 2 8-8M13 21h9"/></svg>Matters</div>
    <div class="add-item"><svg viewBox="0 0 24 24" fill="none" stroke="#9aa5b3" stroke-width="1.8"><circle cx="12" cy="8" r="4"/><path d="M4 21c0-5 3-7 8-7s8 2 8 7z"/></svg>Contact</div>
  </div>
</div>
</body>
</html>
```